Public Relations Agency Seeks Wordpress Design and Coding

TORVEX Media is a public relations agency specializing in media relations, public affairs and marketing communication.

The site should display the following visual characteristics: professionalism, trustworthiness, high-tech focus, clear and concise design.

The desired colors are royal blue, gray and hints of red.

Design look/feel inspired by this site: http://brisklanefetes.example/

Specifications:

1. Navigation/Pages/Index:

HOME

ABOUT US

SERVICES

NEWS

CONTACT

---

2. Functionality of/content for each page:

- Home
o Dominant photo (professional, edgy, innovative)
o Simple, straightforward access to/from “Home” from other pages
o Includes logo (attached) and tagline "Unleash the power of communication"
o Direct link to “CONTACT”
o Links to social media accounts: Facebook, Twitter, LinkedIn

- About Us

o Company profile blurb
o President’s photo with short bio

- Services
o Public Relations
 Strategic communication
 Brand and reputation management
 Community relations
o Media Relations
 News coverage and contacts
 Media training and interview skills
 Crisis communications
o Congressional Affairs
 Public affairs
 Public policy
 Legislative strategy
o Mass Communication
 Speechwriting
 Presentation creation
 Social media
o Marketing Communications
 Business collateral material
 Promotional campaigns
 Special events and tradeshows

- News
o Blog-like page to post information and/or share news from other sites

- Contact
o Standard “Contact Us” form (Name, Email, Phone, Message)
o Direct Contact
 (555) 314-2690
 Marlow@TORVEXmedia.example

Target Market(s)

Small to large businesses specializing in high technology, defense/military, medicine/healthcare, and wide array of professional services.

Industry/Entity Type

Marketing

Font styles to use
Serif
Sans Serif

Colors
0555a3
ec2027
edf3f7

Requirements
Must have
• -- Project reqires DESIGN - and - fully CODED.

-- Strong SEO

-- Optimized for mobile viewing

Thank you!

```html
<!DOCTYPE html>
<html lang="en">
<head>
<meta charset="utf-8">
<title>TORVEX Media — Unleash the Power of Communication</title>
<link rel="stylesheet" href="https://fonts.googleapis.com/css2?family=Questrial&family=Open+Sans:wght@400;600&display=swap">
<style>
:root{
  --blue:#0555a3;
  --blue-deep:#0a3f7e;
  --red:#ec2027;
  --red-dark:#9d1217;
  --ink:#3a3a3a;
  --grey:#7a7a7a;
  --light:#edf3f7;
  --field:#e6e6e6;
  --white:#ffffff;
}
*{box-sizing:border-box;margin:0;padding:0}
html,body{width:1200px;height:2740px;overflow:hidden}
body{font-family:"Open Sans",Arial,sans-serif;color:var(--ink);background:var(--white);position:relative}
.heading{font-family:"Questrial","Helvetica Neue",sans-serif;font-weight:400}

.site-header{height:108px;display:flex;align-items:center;justify-content:space-between;padding:0 185px 0 165px;border-bottom:1px solid #e3e3e3}
.brand{display:flex;flex-direction:column;align-items:center;color:#555;font-family:"Questrial",sans-serif;line-height:1}
.brand-name{font-size:44px;letter-spacing:1px}
.brand-sub{font-size:13px;letter-spacing:9px;margin-top:2px}
.main-nav{display:flex;gap:38px;font-family:"Questrial",sans-serif;font-size:16px}
.main-nav a{color:#333;text-decoration:none}
.main-nav a.active{color:var(--red)}

.hero{position:relative;height:550px;background:linear-gradient(120deg,#c9d3de 0%,#eef1f4 40%,#dfe5ea 70%,#b9c6d3 100%)}
.hero-banner{position:absolute;left:275px;top:197px;width:650px;height:148px;background:rgba(5,85,163,.88);color:#fff;text-align:center;padding-top:20px}
.hero-banner .line1{font-size:52px;letter-spacing:1px;line-height:1.05}
.hero-banner .line2{font-size:34px;line-height:1.2}
.hero-arrow{position:absolute;top:205px}
.hero-arrow.prev{left:38px}
.hero-arrow.next{right:38px}

.band{position:relative;color:#fff;text-align:center}
.band-red{background:var(--red);height:128px;padding-top:30px}
.band-title{font-size:34px;display:flex;align-items:center;justify-content:center;gap:14px;line-height:1}
.band-sub{font-size:12px;letter-spacing:.5px;margin-top:10px;text-transform:uppercase;opacity:.9}
.notch-up{position:absolute;left:588px;bottom:0}
.notch-down{position:absolute;left:588px;top:0}

.about{height:277px;display:flex;align-items:center;padding:0 190px 0 185px;gap:32px}
.portrait{width:188px;height:188px;border-radius:50%;flex:none;background:radial-gradient(circle at 50% 40%,#e9cfb5 0%,#c79f84 45%,#7b3a3e 100%)}
.about-text h2{font-size:18px;color:#333;line-height:1.45;font-family:"Open Sans",sans-serif;font-weight:400}
.about-text p{font-size:11px;color:var(--grey);line-height:1.6;margin-top:10px}

.services{height:433px;background:linear-gradient(180deg,#0555a3,#064c93);color:#fff;text-align:center;padding-top:50px}
.services .band-title{font-size:31px}
.services-sub{font-size:14px;color:#4d86c4;margin-top:12px}
.service-grid{display:flex;justify-content:center;gap:38px;margin-top:35px}
.service{width:238px;display:flex;flex-direction:column;align-items:center}
.service-icon{width:80px;height:80px;border-radius:50%;background:var(--blue-deep);display:flex;align-items:center;justify-content:center}
.service h3{font-size:19px;margin-top:22px;font-family:"Open Sans",sans-serif;font-weight:400}
.service p{font-size:11px;color:#9fbde0;line-height:1.65;margin-top:6px}
.btn-outline{display:inline-block;margin-top:14px;border:2px solid #fff;color:#fff;font-size:10px;padding:6px 16px;text-decoration:none;font-weight:600;letter-spacing:.5px}

.cta{height:210px;text-align:center;padding-top:48px}
.cta h2{font-size:30px;color:var(--red)}
.cta p{font-size:14px;color:var(--grey);margin-top:6px}
.btn-red{display:inline-block;margin-top:22px;background:var(--red);color:#fff;font-size:13px;padding:9px 17px;text-decoration:none;font-weight:600}

.news{position:relative;height:518px;color:#fff;padding-top:54px}
.news-bg{position:absolute;inset:0;background:linear-gradient(110deg,#4a4a4a 0%,#6e6e6e 45%,#575757 75%,#3f3f3f 100%)}
.news-inner{position:relative;text-align:center}
.news .band-title{font-size:32px}
.news-intro{font-size:11px;line-height:1.7;width:720px;margin:18px auto 0}
.news-grid{display:grid;grid-template-columns:424px 380px;column-gap:0;row-gap:40px;margin:32px 0 0 208px;text-align:left}
.news-item h3{font-size:21px;font-family:"Open Sans",sans-serif;font-weight:400}
.news-item p{font-size:11px;line-height:1.6;color:#e4e4e4;margin-top:8px;width:370px}
.news-item a{display:block;color:var(--red);font-size:11px;margin-top:4px;text-decoration:none}

.contact{height:328px;display:flex;padding:55px 0 0 196px}
.address{width:296px}
.contact h3{font-size:19px;color:var(--blue)}
.address .company{font-size:16px;color:#555;margin-top:16px;letter-spacing:.5px}
.address p{font-size:12px;color:var(--grey);line-height:1.95}
.social{display:flex;gap:6px;margin-top:6px}
.social span{width:26px;height:26px;border-radius:50%;background:#111}
.quote-form{display:grid;grid-template-columns:237px 280px;column-gap:11px;margin-top:18px}
.fields{display:flex;flex-direction:column;gap:10px}
.field{height:30px;background:var(--field);font-size:10px;color:#888;padding:9px 12px}
.message{height:110px;background:var(--field);font-size:10px;color:#888;padding:12px}
.btn-blue{width:100px;height:36px;background:var(--blue);color:#fff;font-size:13px;font-weight:600;display:flex;align-items:center;justify-content:center;margin-top:10px}

.site-footer{position:absolute;left:0;right:0;bottom:0;height:60px;background:#f3f3f3;border-top:1px solid #e0e0e0;font-size:10px;color:#666;padding:22px 0 0 196px}
</style>
</head>
<body>

<header class="site-header">
  <a class="brand" href="#" aria-label="TORVEX Media home" style="text-decoration:none">
    <span class="brand-name">TORVEX</span>
    <span class="brand-sub">MEDIA</span>
  </a>
  <nav class="main-nav">
    <a class="active" href="#">HOME</a>
    <a href="#">ABOUT US</a>
    <a href="#">SERVICES</a>
    <a href="#">NEWS</a>
    <a href="#">CONTACT US</a>
  </nav>
</header>

<section class="hero" role="img" aria-label="Photo of a smiling professional team gathered around a meeting table in a bright office">
  <svg class="hero-arrow prev" width="40" height="110" viewBox="0 0 40 110"><polyline points="38,2 2,55 38,108" fill="none" stroke="#fff" stroke-width="2"/></svg>
  <div class="hero-banner heading">
    <div class="line1">UNLEASH THE POWER</div>
    <div class="line2">OF COMMUNICATION</div>
  </div>
  <svg class="hero-arrow next" width="40" height="110" viewBox="0 0 40 110"><polyline points="2,2 38,55 2,108" fill="none" stroke="#fff" stroke-width="2"/></svg>
</section>

<section class="band band-red">
  <h2 class="band-title heading">
    <svg width="18" height="18" viewBox="0 0 24 24"><polygon points="12,1 15,9 23,9 16.5,14 19,22 12,17 5,22 7.5,14 1,9 9,9" fill="var(--red-dark)"/></svg>
    ABOUT&nbsp; COMPANY
    <svg width="18" height="18" viewBox="0 0 24 24"><polygon points="12,1 15,9 23,9 16.5,14 19,22 12,17 5,22 7.5,14 1,9 9,9" fill="var(--red-dark)"/></svg>
  </h2>
  <div class="band-sub">Mauris vel lacus vitae felis vestibulum volutpat</div>
  <svg class="notch-up" width="24" height="14" viewBox="0 0 24 14"><polygon points="0,14 12,0 24,14" fill="#fff"/></svg>
</section>

<section class="about">
  <div class="portrait" role="img" aria-label="Portrait of the agency president"></div>
  <div class="about-text">
    <h2>Curabitur iaculis tempus eros Curabitur vel mi sit amet magna malesuada ultrices nisi erat fermentum vel congue id euismod</h2>
    <p>viverra in gravida eu mattis in ante Morbi eget arcu Morbi porta libero id ullamcorper nonummy nibh ligula pulvinar metus eget consectetuer augue nisi quis lacus Ut ac mi quis lacus mollis aliquam Curabitur iaculis tempus eros Curabitur vel mi sit amet magna malesuada ultrices Ut nisi erat fermentum vel congue id euismod in elit Fusce ultricies orci ac feugiat suscipit leo massa sodales velit et scelerisque mi tortor at ipsum</p>
    <p>cligula augue bibendum accumsan vestibulum ut commodo a mi Morbi ornare gravida elit Integer congue augue et malesuada iaculis ipsum dui aliquet felis at cursus magna nisl nec elit Praesent elementum elit at</p>
  </div>
</section>

<section class="services">
  <h2 class="band-title heading">
    <svg width="17" height="17" viewBox="0 0 24 24"><polygon points="12,1 15,9 23,9 16.5,14 19,22 12,17 5,22 7.5,14 1,9 9,9" fill="var(--blue-deep)"/></svg>
    SERVICES PROVIDE
    <svg width="17" height="17" viewBox="0 0 24 24"><polygon points="12,1 15,9 23,9 16.5,14 19,22 12,17 5,22 7.5,14 1,9 9,9" fill="var(--blue-deep)"/></svg>
  </h2>
  <div class="services-sub">Curabitur vel mi sit amet magna malesuada ultrices&nbsp; nisi erat fermentum</div>
  <div class="service-grid">
    <div class="service">
      <div class="service-icon">
        <svg width="46" height="36" viewBox="0 0 46 36" fill="#fff"><circle cx="12" cy="11" r="6"/><circle cx="34" cy="11" r="6"/><circle cx="23" cy="9" r="7"/><path d="M2 32c0-8 5-12 10-12s10 4 10 12z"/><path d="M24 32c0-8 5-12 10-12s10 4 10 12z"/><path d="M11 34c0-10 6-15 12-15s12 5 12 15z"/></svg>
      </div>
      <h3>Media Relations</h3>
      <p>Morbi diam mauris viverra in gravida eu mattis in ante Morbi eget arcu Morbi porta libero id ullamcorper</p>
      <a class="btn-outline" href="#">LEARN MORE</a>
    </div>
    <div class="service">
      <div class="service-icon">
        <svg width="46" height="40" viewBox="0 0 46 40" fill="#fff"><circle cx="9" cy="8" r="4"/><circle cx="18" cy="6" r="4"/><circle cx="28" cy="6" r="4"/><circle cx="37" cy="8" r="4"/><rect x="5" y="14" width="8" height="16" rx="3"/><rect x="14" y="12" width="8" height="18" rx="3"/><rect x="24" y="12" width="8" height="18" rx="3"/><rect x="33" y="14" width="8" height="16" rx="3"/><path d="M3 36c6-4 34-4 40 0" stroke="#fff" stroke-width="2" fill="none"/></svg>
      </div>
      <h3>Public Affairs</h3>
      <p>Morbi diam mauris viverra in gravida eu mattis in ante Morbi eget arcu Morbi porta libero id ullamcorper</p>
      <a class="btn-outline" href="#">LEARN MORE</a>
    </div>
    <div class="service">
      <div class="service-icon">
        <svg width="46" height="40" viewBox="0 0 46 40"><ellipse cx="18" cy="15" rx="16" ry="12" fill="none" stroke="#fff" stroke-width="3"/><path d="M8 25l-4 8 10-5" fill="#fff"/><ellipse cx="30" cy="22" rx="13" ry="10" fill="#fff"/><path d="M38 29l4 7-9-4z" fill="#fff"/><circle cx="25" cy="22" r="1.8" fill="var(--blue-deep)"/><circle cx="30" cy="22" r="1.8" fill="var(--blue-deep)"/><circle cx="35" cy="22" r="1.8" fill="var(--blue-deep)"/></svg>
      </div>
      <h3>Marketing Communication</h3>
      <p>Morbi diam mauris viverra in gravida eu mattis in ante Morbi eget arcu Morbi porta libero id ullamcorper</p>
      <a class="btn-outline" href="#">LEARN MORE</a>
    </div>
  </div>
</section>

<section class="cta">
  <h2 class="heading">Vivamus porttitor purus nisi eleifend libero a tempus</h2>
  <p>Curabitur vel mi sit amet magna malesuada ultrices&nbsp; nisi erat fermentum</p>
  <a class="btn-red" href="#">LEARN MORE</a>
</section>

<section class="news">
  <div class="news-bg" role="img" aria-label="Muted photo of colleagues talking together in an office"></div>
  <svg class="notch-down" width="24" height="14" viewBox="0 0 24 14" style="position:absolute;z-index:1"><polygon points="0,0 24,0 12,14" fill="#fff"/></svg>
  <div class="news-inner">
    <h2 class="band-title heading">
      <svg width="18" height="18" viewBox="0 0 24 24"><polygon points="12,1 15,9 23,9 16.5,14 19,22 12,17 5,22 7.5,14 1,9 9,9" fill="#fff"/></svg>
      LATEST NEWS
      <svg width="18" height="18" viewBox="0 0 24 24"><polygon points="12,1 15,9 23,9 16.5,14 19,22 12,17 5,22 7.5,14 1,9 9,9" fill="#fff"/></svg>
    </h2>
    <p class="news-intro">Curabitur iaculis tempus eros Curabitur vel mi sit amet magna malesuada ultrices Ut nisi erat fermentum vel congue id euismod in elit Fusce ultricies orci ac feugiat suscipit leo massa sodales velit et scelerisque mi tortor at ipsum</p>
    <div class="news-grid">
      <article class="news-item">
        <h3>Lorem ipsum dolor sit amet</h3>
        <p>Morbi ornare gravida elit Integer congue augue et malesuada iaculis ipsum dui aliquet felis at cursus magna nisl nec elit Praesent elementum elit at tellus nec ultricies sit amet porttitor mattis</p>
        <a href="#">Read More</a>
      </article>
      <article class="news-item">
        <h3>Augue bibendum accumsan</h3>
        <p>Morbi ornare gravida elit Integer congue augue et malesuada iaculis ipsum dui aliquet felis at cursus magna nisl nec elit Praesent elementum elit at tellus nec ultricies sit amet</p>
        <a href="#">Read More</a>
      </article>
      <article class="news-item">
        <h3>Morbi porta libero ullamcorper</h3>
        <p>Morbi ornare gravida elit Integer congue augue et malesuada iaculis ipsum dui aliquet felis at cursus magna nisl nec elit Praesent elementum elit at tellus nec ultricies sit amet porttitor mattis</p>
        <a href="#">Read More</a>
      </article>
      <article class="news-item">
        <h3>Fusce ultricies orci feugiat</h3>
        <p>Morbi ornare gravida elit Integer congue augue et malesuada iaculis ipsum dui aliquet felis at cursus magna nisl nec elit Praesent elementum elit at tellus nec ultricies sit amet</p>
        <a href="#">Read More</a>
      </article>
    </div>
  </div>
</section>

<section class="band band-red">
  <h2 class="band-title heading">
    <svg width="18" height="18" viewBox="0 0 24 24"><polygon points="12,1 15,9 23,9 16.5,14 19,22 12,17 5,22 7.5,14 1,9 9,9" fill="var(--red-dark)"/></svg>
    CONTACT US
    <svg width="18" height="18" viewBox="0 0 24 24"><polygon points="12,1 15,9 23,9 16.5,14 19,22 12,17 5,22 7.5,14 1,9 9,9" fill="var(--red-dark)"/></svg>
  </h2>
  <div class="band-sub">Mauris vel lacus vitae felis vestibulum volutpat</div>
  <svg class="notch-up" width="24" height="14" viewBox="0 0 24 14"><polygon points="0,14 12,0 24,14" fill="#fff"/></svg>
</section>

<section class="contact">
  <div class="address">
    <h3 class="heading">Address</h3>
    <div class="company heading">TORVEX MEDIA LTD</div>
    <p>48 Quarry Row #2B<br>Texas 75001 TX<br>Phone: 555.201.4476<br>Email: info@torvexmedia.example</p>
    <div class="social" aria-label="Social media links"><span></span><span></span><span></span></div>
  </div>
  <div class="quote">
    <h3 class="heading">Get a Quote</h3>
    <div class="quote-form">
      <div class="fields">
        <div class="field">Full Name</div>
        <div class="field">Email address</div>
        <div class="field">Phone no.</div>
      </div>
      <div class="message">Message</div>
    </div>
    <div class="btn-blue">SUBMIT</div>
  </div>
</section>

<footer class="site-footer">© 2014 Company Name&nbsp; All right reserved&nbsp; Term of Use</footer>

</body>
</html>
```